Brackenly.com Postcard

We want to create a postcard, which is going to be mailed out to 6k managers at Hospitals throughout the USA.

I attached a rough draft of what I want the postcard to look like, but want it to look much better. The postcard size is 5.47" * 4.21"

```html
<!DOCTYPE html>
<html lang="en">
<head>
<meta charset="utf-8">
<title>Brackenly Medical Postcard</title>
<link rel="stylesheet" href="https://fonts.googleapis.com/css2?family=Nunito+Sans:wght@400;600;700;800&family=Arimo:wght@400;700&display=swap">
<style>
  :root {
    --canvas: #ebebeb;
    --paper: #ffffff;
    --navy: #24234f;
    --navy-deep: #1c2459;
    --blue: #1a9bd7;
    --blue-mid: #0d6fae;
    --photo-light: #eef2f6;
    --photo-mid: #c9d6e3;
    --rule: #3a3866;
  }
  * { box-sizing: border-box; margin: 0; padding: 0; }
  html, body { width: 1200px; height: 1000px; overflow: hidden; background: var(--canvas); }
  body { position: relative; font-family: "Nunito Sans", sans-serif; color: var(--navy); }

  .postcard { position: absolute; width: 563px; height: 435px; background: var(--paper); overflow: hidden; }
  .postcard--front { left: 122px; top: 55px; }
  .postcard--back { left: 542px; top: 510px; }

  .front-art { position: absolute; inset: 0; }

  .brand { position: absolute; display: flex; align-items: center; gap: 8px;
    font-family: "Nunito Sans", sans-serif; font-weight: 700; font-size: 21px;
    color: var(--navy); letter-spacing: 0.5px; }
  .brand-mark { width: 22px; height: 22px; border-radius: 50%; background: var(--navy); }
  .postcard--front .brand { left: 14px; top: 30px; }
  .postcard--back .brand { left: 28px; top: 31px; }

  .offer { position: absolute; left: 0; width: 410px; top: 106px; text-align: center; }
  .offer-title { font-size: 32px; font-weight: 800; line-height: 1; }
  .offer-sub { margin-top: 10px; font-size: 15px; font-weight: 700; }
  .offer-points { list-style: none; margin-top: 5px; font-size: 14px; line-height: 21px; }
  .offer-cta { position: absolute; left: 18px; top: 264px; font-size: 13px; font-weight: 800; text-transform: uppercase; }

  .call-box { position: absolute; left: 106px; top: 296px; width: 182px; height: 69px; border-radius: 7px;
    background: linear-gradient(var(--blue-mid), var(--navy-deep)); text-align: center; color: #fff;
    box-shadow: 0 2px 4px rgba(0,0,0,.35); overflow: hidden; }
  .call-label { font-size: 14px; font-weight: 800; line-height: 22px; }
  .call-phone { background: #fff; color: var(--navy); font-size: 20px; font-weight: 800; line-height: 24px; }
  .call-web { font-size: 14px; line-height: 22px; }

  .contact { font-family: "Arimo", sans-serif; }
  .contact-name { font-family: "Nunito Sans", sans-serif; font-weight: 800; }
  .postcard--front .contact { position: absolute; right: 14px; top: 350px; text-align: right; color: #fff; font-size: 12.5px; line-height: 15.5px; }
  .postcard--front .contact-name { font-size: 16px; line-height: 20px; }

  .back-title { position: absolute; left: 22px; top: 142px; font-size: 26px; font-weight: 800; }
  .stamp-box { position: absolute; left: 418px; top: 34px; width: 112px; height: 112px; border: 2px solid var(--rule); }
  .address-line { position: absolute; left: 300px; width: 230px; height: 2px; background: var(--rule); }
  .postcard--back .contact { position: absolute; left: 0; width: 292px; top: 300px; text-align: center; font-size: 11px; line-height: 14px; }
  .postcard--back .contact-name { font-size: 15px; line-height: 18px; }
</style>
</head>
<body>

<section class="postcard postcard--front">
  <svg class="front-art" width="563" height="435" viewBox="0 0 563 435">
    <defs>
      <linearGradient id="photoTone" x1="0" y1="0" x2="1" y2="1">
        <stop offset="0" stop-color="#f4f6f9"/>
        <stop offset="0.6" stop-color="#dde6ef"/>
        <stop offset="1" stop-color="#c4d3e2"/>
      </linearGradient>
      <linearGradient id="band" x1="0" y1="0" x2="1" y2="0">
        <stop offset="0" stop-color="#1a9bd7"/>
        <stop offset="0.45" stop-color="#16559a"/>
        <stop offset="1" stop-color="#1f2a5c"/>
      </linearGradient>
      <linearGradient id="swoosh" x1="0" y1="0" x2="0" y2="1">
        <stop offset="0" stop-color="#2ab0e6"/>
        <stop offset="1" stop-color="#0c7fc0"/>
      </linearGradient>
    </defs>
    <rect width="563" height="435" fill="url(#photoTone)" role="img" aria-label="Photo of a smiling doctor with stethoscope and medical staff behind him"/>
    <path d="M0 0 H563 V25 C420 50 200 75 0 110 Z" fill="#fff"/>
    <path d="M0 110 C200 75 420 50 563 25" fill="none" stroke="#c9ccd4" stroke-width="1.5"/>
    <path d="M0 355 C120 362 215 395 250 435 H0 Z" fill="url(#swoosh)"/>
    <path d="M0 410 C90 385 190 372 300 380" fill="none" stroke="#fff" stroke-width="1.5"/>
    <path d="M290 435 C330 360 420 330 563 313 V435 Z" fill="url(#band)"/>
  </svg>

  <div class="brand"><span class="brand-mark"></span>BRACKENLY MEDICAL</div>

  <div class="offer">
    <h1 class="offer-title">We Buy IV Pump</h1>
    <p class="offer-sub">Looking To Sell Your Infusion IV Pumps?</p>
    <ul class="offer-points">
      <li>Brackenly Medical will purchase your infusion iv pumps</li>
      <li>We will buy all of your quality iv pumps</li>
      <li>We offer competitive pricing</li>
      <li>We will purchase from companies and individuals</li>
    </ul>
  </div>
  <p class="offer-cta">Sell infusion pumps to Brackenly Medical today !!</p>

  <div class="call-box">
    <p class="call-label">CALL US TODAY!!</p>
    <p class="call-phone">919-555-0143</p>
    <p class="call-web">www.brackenly.com</p>
  </div>

  <address class="contact">
    <p class="contact-name">BRACKENLY MEDICAL</p>
    <p>Fernbrook, NC 27000 . PO Box 2210</p>
    <p>Phone: 919-555-0143 | Fax: 888-555-0198</p>
    <p>Email: sales@brackenly.com | www.brackenly.com</p>
  </address>
</section>

<section class="postcard postcard--back">
  <div class="brand"><span class="brand-mark"></span>BRACKENLY MEDICAL</div>
  <div class="stamp-box"></div>
  <h2 class="back-title">“We Buy IV Pump!”</h2>
  <span class="address-line" style="top:200px"></span>
  <span class="address-line" style="top:229px"></span>
  <span class="address-line" style="top:257px"></span>
  <span class="address-line" style="top:285px"></span>
  <address class="contact">
    <p class="contact-name">BRACKENLY MEDICAL</p>
    <p>Fernbrook, NC 27000 . PO Box 2210</p>
    <p>Phone: 919-555-0143 | Fax: 888-555-0198</p>
    <p>Email: sales@brackenly.com | www.brackenly.com</p>
  </address>
</section>

</body>
</html>
```